Harbourline Works Group Business Card Redesign

Logo has already been developed. The current business card is one sided. We'd like our mission on the back and more creativity so it pops. We may also like a tagline on the back
One call...all the service, all the savings. Examples are attached from our printer but we don't like them. The front is how we have our existing cards but the back is new. We are open to all ideas. We do like our colors/ brand of purple, black, white...

```html
<!DOCTYPE html>
<html lang="en">
<head>
<meta charset="utf-8">
<title>Harbourline Works Group – Business Card Back</title>
<link rel="stylesheet" href="https://fonts.googleapis.com/css2?family=Montserrat:wght@300;400;600&display=swap">
<style>
  :root {
    --purple-top: #5e2f86;
    --purple-mid: #4a2a6c;
    --purple-deep: #35214f;
    --night: #1d1729;
    --night-edge: #2a2040;
    --glow: #c9a3e6;
    --white: #ffffff;
    --ghost: rgba(255, 255, 255, 0.16);
  }
  html, body {
    margin: 0;
    padding: 0;
    width: 1200px;
    height: 720px;
    overflow: hidden;
    background: var(--night);
  }
  .card {
    position: relative;
    width: 1200px;
    height: 720px;
    overflow: hidden;
    background: linear-gradient(180deg, var(--purple-top) 0%, var(--purple-mid) 45%, var(--purple-deep) 70%);
    font-family: "Montserrat", sans-serif;
    color: var(--white);
  }
  .card-backdrop {
    position: absolute;
    inset: 0;
    width: 1200px;
    height: 720px;
  }
  .ghost-heading {
    position: absolute;
    left: 150px;
    top: 118px;
    margin: 0;
    font-size: 84px;
    font-weight: 600;
    letter-spacing: 2px;
    color: var(--ghost);
    filter: blur(5px);
    white-space: nowrap;
  }
  .brand-name {
    position: absolute;
    right: 70px;
    top: 92px;
    display: flex;
    align-items: center;
    gap: 12px;
    font-size: 26px;
    font-weight: 600;
    line-height: 1.1;
    color: var(--white);
    text-align: left;
  }
  .brand-dot {
    width: 16px;
    height: 16px;
    border-radius: 50%;
    background: var(--white);
    flex: none;
  }
  .mission-heading {
    position: absolute;
    left: 210px;
    top: 166px;
    margin: 0;
    font-size: 34px;
    font-weight: 600;
    letter-spacing: 0.5px;
  }
  .mission-text {
    position: absolute;
    left: 154px;
    top: 228px;
    width: 700px;
    margin: 0;
    font-size: 34px;
    font-weight: 300;
    line-height: 43px;
    letter-spacing: -0.3px;
  }
  .tagline {
    position: absolute;
    left: 0;
    right: 0;
    top: 600px;
    margin: 0;
    display: flex;
    justify-content: center;
    align-items: center;
    gap: 28px;
    font-size: 36px;
    font-weight: 400;
    letter-spacing: 0.5px;
    white-space: nowrap;
  }
  .tagline-divider {
    width: 11px;
    height: 11px;
    border-radius: 50%;
    background: var(--white);
  }
</style>
</head>
<body>
  <main class="card">
    <svg class="card-backdrop" viewBox="0 0 1200 720" aria-hidden="true">
      <defs>
        <linearGradient id="lower-band" x1="0" y1="0" x2="0" y2="1">
          <stop offset="0" stop-color="#2b2042"/>
          <stop offset="0.35" stop-color="var(--night)"/>
          <stop offset="1" stop-color="#17121f"/>
        </linearGradient>
        <linearGradient id="rim-light" x1="0" y1="0" x2="1" y2="0">
          <stop offset="0" stop-color="#8a6fb0" stop-opacity="0.5"/>
          <stop offset="0.6" stop-color="#7c5aa6" stop-opacity="0.3"/>
          <stop offset="0.9" stop-color="var(--glow)" stop-opacity="0.95"/>
          <stop offset="1" stop-color="var(--glow)" stop-opacity="0.7"/>
        </linearGradient>
        <radialGradient id="soft-glow" cx="0.5" cy="0.5" r="0.5">
          <stop offset="0" stop-color="#8e5cbc" stop-opacity="0.35"/>
          <stop offset="1" stop-color="#8e5cbc" stop-opacity="0"/>
        </radialGradient>
      </defs>
      <ellipse cx="560" cy="200" rx="620" ry="260" fill="url(#soft-glow)"/>
      <path d="M -40 120 C 200 20, 700 -10, 1020 60 C 1140 90, 1210 160, 1200 240"
            fill="none" stroke="#7a52a0" stroke-opacity="0.35" stroke-width="3"/>
      <path d="M 0 472 C 250 500, 620 540, 880 470 C 1010 435, 1120 380, 1200 320 L 1200 720 L 0 720 Z"
            fill="url(#lower-band)"/>
      <path d="M 0 472 C 250 500, 620 540, 880 470 C 1010 435, 1120 380, 1200 320"
            fill="none" stroke="url(#rim-light)" stroke-width="4"/>
      <path d="M 0 560 C 300 560, 700 510, 940 450 C 1060 420, 1150 380, 1200 350"
            fill="none" stroke="#5b3f85" stroke-opacity="0.45" stroke-width="3"/>
    </svg>

    <p class="ghost-heading" aria-hidden="true">OUR MISSION</p>

    <div class="brand-name">
      <span class="brand-dot"></span>
      <span>Harbourline<br>Works Group</span>
    </div>

    <h2 class="mission-heading">OUR MISSION</h2>
    <p class="mission-text">To ensure the injured worker returns to function and work, faster, better, stronger while creating longterm client loyalty through service and value we provide.</p>

    <p class="tagline">
      <span>ONE CALL</span>
      <span class="tagline-divider" aria-hidden="true"></span>
      <span>ALL THE SERVICE</span>
      <span class="tagline-divider" aria-hidden="true"></span>
      <span>ALL THE SAVINGS</span>
    </p>
  </main>
</body>
</html>
```